Real Estate Card Design

I need a new business card! Below you will find my headshot, the company logo and a copy of my previous business card.

The card must contain the following information:

Dana Welch
Sales Representative
FAIR HARBOUR HOMES REALTY INC BROKERGE
204-517 Maple Ave E, Oshawa ON L1G 4K7
Cell: 905-618-4037 Office:905-481-2696
www.danawelch.com dana@movewithwelch.ca

I would like the card to portray security and class all the while being fresh and contemporary. I hold the key....

```html
<!DOCTYPE html>
<html lang="en">
<head>
<meta charset="utf-8">
<title>Dana Welch – Business Card</title>
<link href="https://fonts.googleapis.com/css2?family=Nunito+Sans:wght@400;600;700&family=Nunito:ital,wght@1,800&display=swap" rel="stylesheet">
<style>
  :root {
    --page: #ffffff;
    --card: #000000;
    --brand-panel: #06090a;
    --brand-blue: #27a3dd;
    --streak-deep: #0a1a3a;
    --streak-bright: #1aa8e8;
    --portrait-tone: #3a3a44;
    --text: #ffffff;
    --url: #d8b49e;
  }
  html, body {
    margin: 0;
    width: 1200px;
    height: 1000px;
    overflow: hidden;
    background: var(--page);
  }
  .business-card {
    position: absolute;
    left: 301px;
    top: 284px;
    width: 615px;
    height: 360px;
    border-radius: 22px;
    background: var(--card);
    overflow: hidden;
    font-family: "Nunito Sans", sans-serif;
    color: var(--text);
  }
  .light-streaks {
    position: absolute;
    left: 270px;
    top: 0;
    width: 345px;
    height: 360px;
    background:
      radial-gradient(ellipse 70% 40% at 75% 30%, rgba(26,168,232,0.85), transparent 70%),
      linear-gradient(160deg, transparent 0%, var(--streak-deep) 35%, var(--streak-bright) 60%, var(--streak-deep) 85%, transparent 100%);
    opacity: 0.9;
  }
  .agent-portrait {
    position: absolute;
    left: 405px;
    top: 112px;
    width: 210px;
    height: 248px;
    border-radius: 90px 90px 0 0;
    background: linear-gradient(180deg, #b89a7a 0%, var(--portrait-tone) 55%, #15151a 100%);
  }
  .website {
    position: absolute;
    left: 345px;
    top: 70px;
    font-family: "Nunito", sans-serif;
    font-style: italic;
    font-weight: 800;
    font-size: 21px;
    letter-spacing: 1px;
    color: var(--url);
    text-shadow: 1px 1px 2px rgba(0,0,0,0.7);
    transform: rotate(-19deg);
    transform-origin: left bottom;
    white-space: nowrap;
  }
  .brand-panel {
    position: absolute;
    left: 19px;
    top: 21px;
    width: 263px;
    height: 152px;
    background: var(--brand-panel);
  }
  .brand-mark {
    position: absolute;
    left: 80px;
    top: 11px;
    width: 106px;
    height: 62px;
    background: var(--brand-blue);
  }
  .brand-name {
    position: absolute;
    left: 0;
    top: 80px;
    width: 263px;
    text-align: center;
    font-weight: 700;
    font-size: 18px;
    line-height: 22px;
    color: var(--text);
    letter-spacing: 0.5px;
  }
  .agent-name {
    position: absolute;
    left: 104px;
    top: 185px;
    margin: 0;
    font-size: 20px;
    font-weight: 600;
  }
  .agent-title {
    position: absolute;
    left: 104px;
    top: 213px;
    margin: 0;
    font-size: 15px;
    font-weight: 400;
  }
  .contact-list {
    position: absolute;
    left: 102px;
    top: 243px;
    margin: 0;
    padding: 0;
    list-style: none;
  }
  .contact-item {
    display: flex;
    align-items: center;
    gap: 8px;
    height: 26px;
    font-size: 16.5px;
  }
  .contact-item.email { font-size: 14px; height: 22px; }
  .contact-item.address { font-size: 14px; margin-top: 10px; }
  .contact-icon { width: 18px; height: 18px; flex: none; fill: var(--brand-blue); }
</style>
</head>
<body>
  <div class="business-card">
    <div class="light-streaks" role="img" aria-label="Blue light streaks background"></div>
    <div class="agent-portrait" role="img" aria-label="Portrait of the agent holding a house key"></div>
    <div class="website">www.danawelch.com</div>

    <div class="brand-panel">
      <div class="brand-mark"></div>
      <div class="brand-name">FAIR HARBOUR HOMES<br>REALTY INC. BROKERAGE</div>
    </div>

    <h1 class="agent-name">Dana Welch</h1>
    <p class="agent-title">Sales Representative</p>

    <ul class="contact-list">
      <li class="contact-item">
        <svg class="contact-icon" viewBox="0 0 18 18"><path d="M5 1h8a1.5 1.5 0 0 1 1.5 1.5v13A1.5 1.5 0 0 1 13 17H5a1.5 1.5 0 0 1-1.5-1.5v-13A1.5 1.5 0 0 1 5 1zm0.5 2v10h7V3zM9 14a1 1 0 1 0 0 2a1 1 0 0 0 0-2z"/></svg>
        <span>905-618-4037</span>
      </li>
      <li class="contact-item">
        <svg class="contact-icon" viewBox="0 0 18 18"><path d="M4 1l3 4-2 2c1 2.5 3.5 5 6 6l2-2 4 3-2 3C8 16 2 10 1 3z"/></svg>
        <span>905-481-2696</span>
      </li>
      <li class="contact-item email">
        <svg class="contact-icon" viewBox="0 0 18 18"><path d="M1 4h16v10H1zm1.5 1.2v.3L9 10l6.5-4.5v-.3zM2.5 7.3v5.5h13V7.3L9 11.8z"/></svg>
        <span>dana@movewithwelch.ca</span>
      </li>
      <li class="contact-item address">
        <svg class="contact-icon" viewBox="0 0 18 18"><path d="M9 0a6 6 0 0 0-6 6c0 4.5 6 12 6 12s6-7.5 6-12a6 6 0 0 0-6-6zm0 3.5a2.5 2.5 0 1 1 0 5a2.5 2.5 0 0 1 0-5z"/></svg>
        <span>204-517 Maple Ave E, Oshawa ON L1G 4K7</span>
      </li>
    </ul>
  </div>
</body>
</html>
```